BOLD & MINIMALIST DESIGN NEEDED

We want a very bold but minimalistic business card design that is impactful and utilizes both sides of the business card. Our current logo is included for your use.

We want bold fonts and good use of negative space. We don't want the logo to overpower the design.

Target Market(s)

Professionals who are building new commercial buildings.

Industry/Entity Type

Construction

Contact Information for Business Card

Name, Title, email, office phone, cell phone, website

Font styles to use
Serif
Sans Serif

Requirements
Must have
• Bold design!

```html
<!DOCTYPE html>
<html lang="en">
<head>
<meta charset="utf-8">
<title>Ridgeline Design + Build — Business Card</title>
<link href="https://fonts.googleapis.com/css2?family=Montserrat:wght@400;500;700;900&display=swap" rel="stylesheet">
<style>
  :root {
    --bg: #2a2a2a;
    --lime-light: #dcebc6;
    --lime: #b3d97a;
    --accent: #7dc242;
    --ink: #111111;
    --paper: #ffffff;
    --muted: #333333;
  }
  * { margin: 0; padding: 0; box-sizing: border-box; }
  html, body { width: 1200px; height: 875px; overflow: hidden; }
  body {
    background: var(--bg);
    font-family: "Montserrat", sans-serif;
    position: relative;
  }
  .card {
    position: absolute;
    width: 540px;
    height: 309px;
    border-radius: 22px;
    overflow: hidden;
    box-shadow: 0 18px 40px rgba(0,0,0,0.45);
  }
  /* Front */
  .card-front {
    left: 60px; top: 90px;
    background: linear-gradient(120deg, var(--lime-light) 0%, var(--lime) 100%);
    display: flex; align-items: center; justify-content: center;
  }
  .wordmark { text-align: center; color: var(--ink); }
  .wordmark-name {
    font-weight: 900; font-size: 50px; letter-spacing: 1px; line-height: 1;
    display: flex; align-items: center; gap: 14px; justify-content: center;
  }
  .wordmark-dot { width: 18px; height: 18px; background: var(--ink); }
  .wordmark-rule { height: 2px; background: var(--ink); margin: 8px 0 6px; }
  .wordmark-tag { font-weight: 500; font-size: 15px; letter-spacing: 9px; }

  /* Back */
  .card-back {
    left: 600px; top: 476px;
    background: var(--paper);
  }
  .back-swoosh { position: absolute; right: 0; bottom: 0; }
  .person {
    position: absolute; right: 34px; top: 28px; text-align: right;
  }
  .person-name { color: var(--accent); font-weight: 700; font-size: 22px; }
  .person-title { color: var(--muted); font-weight: 500; font-size: 11px; margin-top: 2px; }
  .back-wordmark { position: absolute; left: 34px; top: 112px; color: var(--ink); }
  .back-wordmark .wordmark-name { font-size: 34px; justify-content: flex-start; }
  .back-wordmark .wordmark-tag { font-size: 11px; letter-spacing: 6px; }
  .back-wordmark .wordmark-rule { margin: 5px 0 4px; }
  .contacts {
    position: absolute; left: 34px; bottom: 30px;
    list-style: none; font-size: 12px; color: var(--muted);
  }
  .contacts li { display: flex; align-items: center; gap: 8px; line-height: 20px; }
  .contacts svg { width: 12px; height: 12px; fill: var(--accent); }
</style>
</head>
<body>
  <section class="card card-front">
    <div class="wordmark">
      <div class="wordmark-name">RIDGELINE</div>
      <div class="wordmark-rule"></div>
      <div class="wordmark-tag">DESIGN + BUILD</div>
    </div>
  </section>

  <section class="card card-back">
    <svg class="back-swoosh" width="260" height="140" viewBox="0 0 260 140" aria-hidden="true">
      <path d="M0 140 C40 60 140 10 260 0 L260 140 Z" fill="var(--ink)"/>
    </svg>
    <div class="person">
      <div class="person-name">Daniel Brooks</div>
      <div class="person-title">CEO &amp; Founder</div>
    </div>
    <div class="back-wordmark">
      <div class="wordmark-name">RIDGELINE</div>
      <div class="wordmark-rule"></div>
      <div class="wordmark-tag">DESIGN + BUILD</div>
    </div>
    <ul class="contacts">
      <li><svg viewBox="0 0 24 24"><path d="M6.6 10.8a15.1 15.1 0 0 0 6.6 6.6l2.2-2.2c.3-.3.7-.4 1-.2 1.1.4 2.3.6 3.6.6.6 0 1 .4 1 1V20c0 .6-.4 1-1 1A17 17 0 0 1 3 4c0-.6.4-1 1-1h3.5c.6 0 1 .4 1 1 0 1.3.2 2.5.6 3.6.1.3 0 .7-.2 1z"/></svg>(555) 214-0384</li>
      <li><svg viewBox="0 0 24 24"><path d="M4 8h16v12H4z M7 3h10v4H7z"/></svg>1-800-555-0142</li>
      <li><svg viewBox="0 0 24 24"><path d="M2 5h20v14H2z M2 5l10 8 10-8" stroke="#fff" stroke-width="1.5"/></svg>info@ridgelinebuild.com</li>
      <li><svg viewBox="0 0 24 24"><circle cx="12" cy="12" r="10"/></svg>www.ridgelinebuild.com</li>
    </ul>
  </section>
</body>
</html>
```